Business card for Tolvery Anesthesia LLC

This is for a business care for Tolvery Anesthesia LLC. Dr. Lisbeth Tolvery, CRNA, DNAP is the sole provider in the LLC. Business address is 4718 N Brackley Street,
Oakhaven, PA 17342
CRNA stands for certified registered nurse anesthetist
"Keeping you safe and comfortable"
I plan to give this business card to the patients that I provide anesthesia to.
Creative design that ties into Anesthesia. Calm soothing colors.

Target Market(s)

Business card for my patients.

Industry/Entity Type

Medicine

Contact Information for Business Card

Creative, professional, eye catching

Logo Text

Tolvery Anesthesia

Font styles to use
Serif
Script

Colors

Designer to choose colors to be used in the design.

Requirements
Must have
• Tolvery Anesthesia
• Dr. Lisbeth Tolvery, CRNA, DNAP
• tolvery.anesthesia@ quillmail.net
Nice to have
• "Keeping you safe and comfortable"
Should not have
• phone number

```html
<!DOCTYPE html>
<html lang="en">
<head>
<meta charset="utf-8">
<title>Tolvery Anesthesia LLC – Business Card</title>
<link rel="stylesheet" href="https://fonts.googleapis.com/css2?family=Cinzel:wght@400;500&family=Montserrat:ital,wght@0,400;0,700;1,400&display=swap">
<style>
  :root {
    --teal: #10878f;
    --grey: #929292;
    --ink: #2b2b2b;
    --paper: #ffffff;
    --backdrop: #ffffff;
  }
  * { margin: 0; padding: 0; box-sizing: border-box; }
  html, body { width: 1200px; height: 1200px; overflow: hidden; background: var(--backdrop); }
  .canvas { position: relative; width: 1200px; height: 1200px; }

  /* brand lockup */
  .brand-lockup {
    position: absolute; left: 150px; top: 170px; width: 300px;
    display: flex; flex-direction: column; align-items: center; gap: 16px;
  }
  .brand-dot { width: 90px; height: 90px; border-radius: 50%; border: 8px solid var(--teal); }
  .brand-name {
    font-family: "Cinzel", serif; font-weight: 500; color: var(--teal);
    font-size: 38px; line-height: 1.1; text-align: center; letter-spacing: 1px;
  }

  /* card */
  .card {
    position: absolute; left: 170px; top: 580px; width: 860px; height: 500px;
    background: var(--paper); box-shadow: 2px 4px 10px rgba(0,0,0,0.28);
  }
  .card-brand {
    position: absolute; top: 70px; left: 0; right: 0;
    display: flex; flex-direction: column; align-items: center; gap: 12px;
  }
  .card-brand .brand-dot { width: 52px; height: 52px; border-width: 5px; }
  .card-brand .brand-name { font-size: 30px; }
  .tagline {
    position: absolute; top: 262px; left: 0; right: 0; text-align: center;
    font-family: "Cinzel", serif; color: var(--teal); font-size: 24px; letter-spacing: 0.5px;
  }
  .holder { position: absolute; top: 340px; left: 60px; width: 360px; text-align: center; }
  .holder-name {
    font-family: "Montserrat", sans-serif; font-weight: 700; color: var(--teal);
    font-size: 25px; letter-spacing: 0.5px; text-transform: uppercase;
  }
  .holder-title {
    font-family: "Montserrat", sans-serif; font-style: italic; color: var(--ink);
    font-size: 24px; margin-top: 4px;
  }
  .contacts {
    position: absolute; top: 340px; left: 470px; list-style: none;
    font-family: "Montserrat", sans-serif; font-size: 18px; color: var(--ink); line-height: 1.3;
  }
  .contacts li { display: flex; gap: 14px; margin-bottom: 12px; }
  .contact-icon { flex: none; width: 18px; height: 18px; margin-top: 2px; }
  .band { position: absolute; bottom: 0; height: 25px; }
  .band-grey { left: 0; width: 428px; background: var(--grey); }
  .band-teal { left: 434px; right: 0; background: var(--teal); }
</style>
</head>
<body>
<main class="canvas">
  <div class="brand-lockup">
    <div class="brand-dot"></div>
    <div class="brand-name">Tolvery<br>Anesthesia LLC</div>
  </div>

  <section class="card">
    <div class="card-brand">
      <div class="brand-dot"></div>
      <div class="brand-name">Tolvery Anesthesia LLC</div>
    </div>
    <p class="tagline">Keeping you safe and comfortable</p>

    <div class="holder">
      <p class="holder-name">Dr. Lisbeth Tolvery</p>
      <p class="holder-title">CRNA, DNAP</p>
    </div>

    <ul class="contacts">
      <li>
        <svg class="contact-icon" viewBox="0 0 18 18"><rect width="18" height="18" fill="#10878f"/><path d="M4 9 L9 4.5 L14 9 H12.5 V13.5 H5.5 V9 Z" fill="#fff"/></svg>
        <span>4718 N Brackley Street,<br>Oakhaven, PA 17342</span>
      </li>
      <li>
        <svg class="contact-icon" viewBox="0 0 18 18"><rect width="18" height="18" fill="#10878f"/><rect x="4" y="5.5" width="10" height="7" fill="none" stroke="#fff" stroke-width="1.2"/><path d="M4 5.5 L9 9.5 L14 5.5" fill="none" stroke="#fff" stroke-width="1.2"/></svg>
        <span>tolvery.anesthesia@ quillmail.net</span>
      </li>
      <li>
        <svg class="contact-icon" viewBox="0 0 18 18"><rect width="18" height="18" fill="#10878f"/><circle cx="9" cy="9" r="5" fill="none" stroke="#fff" stroke-width="1.2"/><path d="M4 9 H14 M9 4 C6.5 7 6.5 11 9 14 M9 4 C11.5 7 11.5 11 9 14" fill="none" stroke="#fff" stroke-width="1"/></svg>
        <span>www.tolvery.anesthesia.com</span>
      </li>
    </ul>

    <div class="band band-grey"></div>
    <div class="band band-teal"></div>
  </section>
</main>
</body>
</html>
```